Design some Business Cards

Create a set of business cards for council of Geodesy.
The cards should be somehow indicative of the level/ status age group of the members, which i why a small description of the stages is included.
The card should look professional and colours and designs should match or complement the initial scheme.

```html
<!DOCTYPE html>
<html lang="en">
<head>
<meta charset="utf-8">
<title>council of Geodesy — Business Cards</title>
<link href="https://fonts.googleapis.com/css2?family=Arimo:wght@400&family=Roboto+Condensed:wght@700&display=swap" rel="stylesheet">
<style>
  :root {
    --page: #e9e7e4;
    --card: #f3f1f2;
    --brand: #6b7d6a;
    --leaf: #8dbf4a;
    --name: #5e7659;
    --ink: #2b2b2b;
    --band-start: #6f9a5f;
    --band-end: #6b7b6c;
  }
  * { margin: 0; padding: 0; box-sizing: border-box; }
  html, body {
    width: 1200px; height: 1200px; overflow: hidden;
    background: var(--page);
    font-family: "Arimo", Arial, sans-serif;
  }
  .card {
    position: absolute; left: 222px;
    width: 756px; height: 432px;
    background: var(--card);
    border-radius: 18px;
    overflow: hidden;
    box-shadow: 0 10px 24px rgba(0,0,0,0.18);
  }
  .card--front { top: 112px; }
  .card--back { top: 616px; }
  .card__band {
    position: absolute; left: 0; right: 0; bottom: 0; height: 28px;
    background: linear-gradient(90deg, var(--band-start), var(--band-end));
  }
  .brand {
    display: flex; align-items: center; gap: 14px;
    color: var(--brand); font-weight: 400; white-space: nowrap;
  }
  .brand__dot { border-radius: 50%; background: var(--leaf); flex: none; }
  .card--front .brand { position: absolute; left: 48px; top: 58px; font-size: 46px; }
  .card--front .brand__dot { width: 30px; height: 30px; }
  .holder { position: absolute; right: 38px; top: 178px; text-align: right; }
  .holder__name {
    font-family: "Roboto Condensed", "Arial Narrow", sans-serif;
    font-weight: 700; font-size: 31px; color: var(--name); letter-spacing: 0.2px;
  }
  .holder__role { font-size: 18px; color: var(--ink); letter-spacing: 1px; margin-top: 2px; }
  .holder__tab {
    position: absolute; right: -38px; top: 4px; width: 32px; height: 26px;
    background: var(--name);
  }
  .contacts { position: absolute; left: 36px; top: 306px; list-style: none; }
  .contacts li {
    display: flex; align-items: center; gap: 12px;
    font-size: 17.5px; color: var(--ink); height: 29px;
  }
  .contacts svg { width: 18px; height: 18px; flex: none; }
  .address {
    position: absolute; right: 42px; top: 336px; text-align: left;
    font-size: 15px; line-height: 28px; color: var(--ink); letter-spacing: 1.3px;
    font-style: normal;
  }
  .card--back .brand {
    position: absolute; left: 0; right: 0; top: 170px;
    justify-content: center; font-size: 58px;
  }
  .card--back .brand__dot { width: 38px; height: 38px; }
  .back__web {
    position: absolute; left: 0; right: 0; top: 368px;
    text-align: center; font-size: 17px; color: var(--brand); letter-spacing: 1px;
  }
</style>
</head>
<body>
  <section class="card card--front">
    <div class="brand"><span class="brand__dot"></span>council of Geodesy</div>
    <div class="holder">
      <span class="holder__tab"></span>
      <div class="holder__name">MARA ELLISON</div>
      <div class="holder__role">FOUNDER</div>
    </div>
    <ul class="contacts">
      <li>
        <svg viewBox="0 0 18 18" aria-hidden="true"><rect x="5" y="1.5" width="8" height="15" rx="1.5" fill="none" stroke="#555" stroke-width="1.6"/><line x1="7.5" y1="13.5" x2="10.5" y2="13.5" stroke="#555" stroke-width="1.4"/></svg>
        00 00 000 00
      </li>
      <li>
        <svg viewBox="0 0 18 18" aria-hidden="true"><circle cx="9" cy="9" r="7.5" fill="#555"/><path d="M5 6c2 0 3 1 2.5 2.5S9 10 8 12.5M11 4c-.5 1.5.5 2.5 2 2.5M12.5 10.5c-1 .5-1.5 2-1 3" stroke="#f3f1f2" stroke-width="1.3" fill="none"/></svg>
        www.yourweb.com
      </li>
      <li>
        <svg viewBox="0 0 18 18" aria-hidden="true"><rect x="1.5" y="4" width="15" height="10" fill="#555"/><path d="M1.5 4l7.5 6 7.5-6" stroke="#f3f1f2" stroke-width="1.3" fill="none"/></svg>
        www.yourmail.com
      </li>
    </ul>
    <address class="address">418 Meridian Lane<br>Halvern HV 20731</address>
    <div class="card__band"></div>
  </section>

  <section class="card card--back">
    <div class="brand"><span class="brand__dot"></span>council of Geodesy</div>
    <div class="back__web">www.yourweb.com</div>
    <div class="card__band"></div>
  </section>
</body>
</html>
```